Label Wanted For New, Millennial, Hard Apple Cider Brand

California, alcoholic apple cider brand targeted towards Millennials needs a label to show product as:

Hand-crafted. Modern. Hipster. Produced from apples. Delicious. Unisex.

We are primarily a small wine producer (500cs/year - 20 barrels/year). Check the attachments for one of our current labels. Tidewhistle will be the name of our cider.

This is the first release of our cider. This cider bottle we will be using is attached (Champagne Mold with a Crown Cap).

We will have several flavors over the course of the next few years and need a placeholder on the front label for the specific style:
"Off-Dry" (Tart + a Little Sweet)
"Dry" (Crisp + Tart)
"Hopped" (Fermented with Hopps)
"HoneyBee" (Fermented with Honey)
"Barrel Aged" (Aged in Barrel)
"Cross Culture" (Fermented with Wine Yeast and Viognier), etc.

Looking for a label that is modern, but also somewhat rustic. Please view our "Labels We Like" file. Something creative and different. Definitely more on the hipster side of things than old-fashioned.
Updates

Project Deadline Extended Reason: Hi designers,We are postponing the deadline due to the holidays. We've been unable to provide effective feedback to many of you with the craziness of Christmas Eve, Christmas and now New Years! Thank you for your patience. We will have feedback for many of you tomorrow and final selections on January 02. Thank you for all of your hard work. - Noor Added Friday, December 26, 2014

Target Market(s)

26-44yr old, educated, outdoorsy, food/wine loving, beer/wine/spirit drinking adults. Unisex product - should be slightly more masculine than feminine.

Industry/Entity Type

Product

Font styles to use
Decorative

Requirements
Must have
• Front:
• 1. Front Label Measurements: Maintain a 4(w) x 4.125(h) inch front with 1/4in bleed.
• 2. Font used for brand name "Tidewhistle" should be legible but unique.
• 3. Artwork should be unisex. Modern with a handcrafted look.
• 4. Front Label Must Contain the Following Info:
• a. "Alc / Vol 7.0%"
• b. California Hard Apple Cider
• c. Placeholder for style of cider (DRY, HOPPED, OFF-DRY, etc.)
• Back Label:
• 1. Back Label Measurements: Maintain a 3(w) x 4.125(h) inch back w/ 1/4in bleed. One back label will be used for all ciders
• 2. Back Label Must Contain the Following Info:
• a. "GOVERNMENT WARNING: (1) ACCORDING TO THE SURGEON GENERAL, WOMEN SHOULD NOT DRINK ALCOHOLIC BEVERAGES DURING PREGNANCY BECAUSE OF THE RISK OF BIRTH DEFECTS. (2) CONSUMPTION OF ALCOHOLIC BEVERAGES IMPAIRS YOUR ABILITY TO DRIVE A CAR OR OPERATE MACHINERY, AND MAY CAUSE HEALTH PROBLEMS."
• b. "CONTAINS SULFITES"
• c. "Produced & Bottled by FM Vine Co, Buellton, CA".
• d. Back label copy. T
• "We Love-love cider. Call us crazy, but we feel that cider just might be the bridge between beer-only drinkers and wine-only drinkers - a white flag of sorts. Go on, shake hands. Finally something we can all agree on. Break free from the norm. Drink what you love. Cheers. Noor K."
Nice to have
• 1. OPEN THE "LABELS I LIKE" FILE. Do not submit a design before looking a this file.
• 2. Label must tie in brand name, "Tide Whistle" with a clever prison reference. Prison bars, barbed wire, a shovel, a prison shank, a spoon used to dig a tunnel, a rock pick, a pick-axe, etc.
• 3. Label must tie in apples / apple trees, etc. Something showing what our cider is made of.
• 4. Label must have a memorable font or a logo for brand recognition that will be congruent across all labels.
Should not have
• NO worms in apples please. People do not want to associate or visualize anything like that for food /beverage products.

```html
<!DOCTYPE html>
<html lang="en">
<head>
<meta charset="utf-8">
<title>Tidewhistle – California Hard Apple Cider Label</title>
<link rel="stylesheet" href="https://fonts.googleapis.com/css2?family=Short+Stack&family=Arvo:wght@700&display=swap">
<style>
  :root {
    --backdrop: #d9d9d9;
    --paper-light: #f4f2ec;
    --paper-warm: #e6dcc6;
    --ink-brown: #5a2712;
    --frame-gold: #d8ad55;
    --frame-rust: #8a4a1c;
    --frame-dark: #4a1a0c;
    --art-tone: #c9b28a;
  }
  * { box-sizing: border-box; margin: 0; padding: 0; }
  html, body {
    width: 1200px;
    height: 793px;
    overflow: hidden;
    background: var(--backdrop);
  }
  .canvas {
    position: relative;
    width: 1200px;
    height: 793px;
  }
  .front-label {
    position: absolute;
    left: 250px;
    top: 84px;
    width: 700px;
    height: 626px;
    padding: 10px;
    background: linear-gradient(180deg, var(--frame-gold) 0%, var(--frame-rust) 65%, var(--frame-dark) 100%);
  }
  .label-face {
    position: relative;
    width: 100%;
    height: 100%;
    background: radial-gradient(ellipse at 40% 35%, var(--paper-light) 0%, var(--paper-light) 45%, var(--paper-warm) 100%);
  }
  .product-line {
    position: absolute;
    left: 29px;
    top: 55px;
    width: 615px;
    height: 42px;
    border: 3px solid var(--ink-brown);
    display: flex;
    align-items: center;
    justify-content: center;
    font-family: "Arvo", serif;
    font-weight: 700;
    font-size: 28px;
    color: var(--ink-brown);
    letter-spacing: 0.5px;
  }
  .character-art {
    position: absolute;
    left: 300px;
    top: 118px;
    width: 367px;
    height: 425px;
  }
  .brand-name {
    position: absolute;
    left: 30px;
    top: 188px;
    font-family: "Short Stack", cursive;
    font-size: 56px;
    font-weight: 400;
    line-height: 1;
    color: var(--ink-brown);
    transform: rotate(-3deg);
    transform-origin: left bottom;
    white-space: nowrap;
  }
  .abv {
    position: absolute;
    left: 64px;
    top: 300px;
    font-family: "Arvo", serif;
    font-weight: 700;
    font-size: 27px;
    color: var(--ink-brown);
  }
  .cider-style {
    position: absolute;
    left: 64px;
    top: 352px;
    padding: 4px 14px;
    border: 3px solid var(--ink-brown);
    font-family: "Arvo", serif;
    font-weight: 700;
    font-size: 22px;
    letter-spacing: 2px;
    text-transform: uppercase;
    color: var(--ink-brown);
  }
</style>
</head>
<body>
  <main class="canvas">
    <section class="front-label">
      <div class="label-face">
        <div class="product-line">California Hard Apple Cider</div>
        <svg class="character-art" role="img" aria-label="Ink illustration of a stout cartoon sheriff in a hat with a star badge, holding a revolver" viewBox="0 0 367 425">
          <defs>
            <radialGradient id="art-wash" cx="50%" cy="55%" r="60%">
              <stop offset="0%" stop-color="var(--art-tone)" stop-opacity="0.55"/>
              <stop offset="100%" stop-color="var(--art-tone)" stop-opacity="0.15"/>
            </radialGradient>
          </defs>
          <path d="M130 0 H300 V190 H367 V425 H0 V200 H130 Z" fill="url(#art-wash)"/>
        </svg>
        <h1 class="brand-name">Tidewhistle</h1>
        <p class="abv">Alc / Vol 7.0%</p>
        <p class="cider-style">Off-Dry</p>
      </div>
    </section>
  </main>
</body>
</html>
```